brikMOSA corporation pty ltd

Contruction industry
It's a wall and floor tiling business

Industry/Entity Type

Business

Requirements
Must have
• Likes-
- clean and easy to read
- a witty design is always well received
- for it to look reputable in the industry
- a strong and direct presentation
- simple but striking colour selection
Should not have
• Dislikes-
- pls no tacky square tiles to resemble tiling

```html
<!DOCTYPE html>
<html lang="en">
<head>
<meta charset="utf-8">
<title>brikMOSA corporation pty ltd – business card</title>
<link rel="stylesheet" href="https://fonts.googleapis.com/css2?family=Open+Sans:wght@400;600;800&display=swap">
<style>
  :root {
    --backdrop: #3b3b3d;
    --card: #ffffff;
    --ink: #111111;
    --ink-soft: #2a2a2a;
    --accent: #f7941d;
    --rule: #8a8a8a;
  }
  * { box-sizing: border-box; margin: 0; padding: 0; }
  html, body {
    width: 1200px;
    height: 534px;
    overflow: hidden;
  }
  body {
    background: var(--backdrop);
    font-family: "Open Sans", Arial, sans-serif;
    color: var(--ink);
    position: relative;
  }
  .card {
    position: absolute;
    top: 119px;
    width: 517px;
    height: 295px;
    background: var(--card);
  }
  .card--front { left: 62px; }
  .card--back  { left: 622px; }

  .wordmark {
    position: absolute;
    display: flex;
    flex-direction: column;
    align-items: flex-end;
    line-height: 1;
  }
  .wordmark__name {
    font-weight: 800;
    color: var(--ink);
    letter-spacing: -0.5px;
  }
  .wordmark__suffix {
    font-weight: 600;
    color: var(--ink);
  }

  .card--front .wordmark {
    left: 80px;
    width: 360px;
    top: 118px;
  }
  .card--front .wordmark__name { font-size: 60px; }
  .card--front .wordmark__suffix { font-size: 14px; margin-top: 2px; }

  .card--front .website {
    position: absolute;
    left: 0;
    right: 0;
    top: 227px;
    text-align: center;
    font-size: 14px;
    letter-spacing: 2.4px;
    color: var(--ink-soft);
  }

  .card--back .wordmark {
    left: 44px;
    width: 219px;
    top: 120px;
  }
  .card--back .wordmark__name { font-size: 36px; }
  .card--back .wordmark__suffix { font-size: 8.5px; margin-top: 1px; }

  .divider {
    position: absolute;
    left: 295px;
    top: 94px;
    width: 1px;
    height: 102px;
    background: var(--rule);
  }

  .contact {
    position: absolute;
    left: 326px;
    top: 90px;
  }
  .contact__name {
    font-size: 16px;
    font-weight: 600;
    color: var(--ink);
    line-height: 1.2;
  }
  .contact__role {
    font-size: 12px;
    color: var(--ink-soft);
    margin-top: 2px;
  }
  .contact__list {
    list-style: none;
    margin-top: 18px;
  }
  .contact__item {
    display: flex;
    align-items: center;
    gap: 6px;
    font-size: 13px;
    color: var(--ink);
    height: 18.5px;
  }
  .contact__icon {
    width: 12px;
    height: 12px;
    flex: none;
  }
</style>
</head>
<body>
  <section class="card card--front" aria-label="Business card front">
    <div class="wordmark">
      <span class="wordmark__name">brikMOSA</span>
      <span class="wordmark__suffix">corporation pty ltd</span>
    </div>
    <p class="website">www.brikmosa.com</p>
  </section>

  <section class="card card--back" aria-label="Business card back">
    <div class="wordmark">
      <span class="wordmark__name">brikMOSA</span>
      <span class="wordmark__suffix">corporation pty ltd</span>
    </div>
    <div class="divider"></div>
    <div class="contact">
      <p class="contact__name">DAN MORELL</p>
      <p class="contact__role">Director</p>
      <ul class="contact__list">
        <li class="contact__item">
          <svg class="contact__icon" viewBox="0 0 12 12" aria-hidden="true">
            <path d="M3 1.2 L4.6 3.6 L3.7 4.6 Q4.6 6.8 7 8.2 L8 7.3 L10.6 8.8 L9.8 10.6 Q5.8 10.8 2.8 7 Q0.9 4.3 1.4 1.9 Z" fill="var(--accent)"/>
          </svg>
          <span>0400 555 128</span>
        </li>
        <li class="contact__item">
          <svg class="contact__icon" viewBox="0 0 12 12" aria-hidden="true">
            <rect x="1" y="2.5" width="10" height="7" fill="none" stroke="var(--accent)" stroke-width="1"/>
            <path d="M1 2.5 L6 6.5 L11 2.5" fill="none" stroke="var(--accent)" stroke-width="1"/>
          </svg>
          <span>dan.mo@mailbox.com</span>
        </li>
        <li class="contact__item">
          <svg class="contact__icon" viewBox="0 0 12 12" aria-hidden="true">
            <g fill="none" stroke="var(--accent)" stroke-width="1">
              <circle cx="6" cy="6" r="4.8"/>
              <ellipse cx="6" cy="6" rx="2" ry="4.8"/>
              <path d="M1.2 6 H10.8 M2 3.6 H10 M2 8.4 H10"/>
            </g>
          </svg>
          <span>www.brikmosa.com</span>
        </li>
      </ul>
    </div>
  </section>
</body>
</html>
```